Introducting Corbin Sheetmetal MADE WITH PRIDE

We require a PDF fact sheet that we can share via email that has a summary of infomation, services and products as found on our website www.corbinsheetmetal.example

The Call to Action - Heading should be "Made with Pride"

Needs to look professional, prefer sharp lines than bubble circles

Trying to attract new business

Target Market(s)

Potential new clients; Plumbers, Shop fitters, restaurants and Caters.

Industry/Entity Type

Manufacturing

Font styles to use
Other font styles liked:
• something masculine

Colors

Designer to choose colors to be used in the design.

Requirements
Must have
• Must be one page, low res so when emailing it's not too large.
• Must have phone number, email address and actual address
• Should include summary of copy from the website; www.corbinsheetmetal.example
• * A bit about us
• * Services
• * Fabrication Range and Finishes
• * General Fabrication
Nice to have
• Something that is not too busy, easy to read - so not too much writing. Must look professional (that's why we using ArtHive).
• Please let me know I you need images from the website and I'll sent to you.
Should not have
• It shouldn't be too busy, easy to read - so not too much writing. Simple and clear message.

```html
<!DOCTYPE html>
<html lang="en">
<head>
<meta charset="utf-8">
<title>Corbin Sheetmetal – Made with Pride</title>
<link href="https://fonts.googleapis.com/css2?family=Arimo:wght@400;700&family=Roboto+Condensed:wght@400;700&family=Oswald:wght@500;700&display=swap" rel="stylesheet">
<style>
:root{
  --stage:#8e8e8e;
  --paper:#ffffff;
  --ink:#1d1d21;
  --text:#3b3b3f;
  --panel:#1f1f24;
  --band:#4f5a55;
  --steel-light:#d9dbdc;
  --steel-mid:#8b8f92;
  --steel-dark:#3c3f43;
  --rule:#222226;
  --tick:#555;
}
*{box-sizing:border-box;margin:0;padding:0}
html,body{width:1200px;height:2574px;overflow:hidden}
body{background:var(--stage);font-family:"Arimo",Arial,sans-serif;color:var(--text)}
.flyer{position:absolute;left:40px;top:495px;width:1120px;height:1584px;background:var(--paper);overflow:hidden;box-shadow:0 10px 30px rgba(0,0,0,.35)}
.hero-photo{position:absolute;left:0;top:0;width:1120px;height:585px;
  background:linear-gradient(100deg,var(--steel-dark) 0%,var(--steel-light) 22%,var(--steel-mid) 40%,#2b2d30 55%,var(--steel-light) 72%,var(--steel-mid) 88%,#cfd2d4 100%)}
.brand-box{position:absolute;right:0;top:0;width:395px;height:242px;background:rgba(255,255,255,.82);display:flex;align-items:center;justify-content:center;gap:14px}
.brand-mark{width:34px;height:34px;background:var(--steel-dark)}
.brand-name{font-family:"Roboto Condensed",sans-serif;font-weight:700;font-size:30px;letter-spacing:1px;color:var(--steel-dark);text-transform:uppercase}
.about{position:absolute;left:0;top:369px;width:509px;height:458px;background:var(--panel);padding:24px 30px 0 30px;color:#f0f0f0}
.about h2{font-family:"Roboto Condensed",sans-serif;font-weight:400;font-size:34px;letter-spacing:1px;padding-bottom:6px;border-bottom:2px solid #fff;margin-bottom:14px;width:270px}
.about p{font-size:15px;line-height:1.3;text-align:justify}
.about p+p{margin-top:14px}
.pride-band{position:absolute;left:522px;top:471px;width:598px;height:114px;background:var(--band);display:flex;align-items:center;justify-content:center}
.pride-band h1{font-family:"Oswald",sans-serif;font-weight:700;font-size:60px;letter-spacing:2px;color:#e4e6e6;text-shadow:0 2px 0 #2a2f2d;text-transform:uppercase}
.services{position:absolute;left:532px;top:610px;width:560px}
.section-title{font-family:"Roboto Condensed",sans-serif;font-weight:700;color:var(--ink);line-height:1}
.services .section-title{font-size:44px;margin-bottom:10px}
.body-text{font-size:15px;line-height:1.27;text-align:justify}
.service-list{display:flex;margin-top:20px;margin-left:30px}
.service-list ul{list-style:none;font-size:15px;line-height:1.5;color:var(--ink)}
.service-list ul:first-child{width:200px;padding-right:14px;border-right:1px solid #999;margin-right:26px}
.service-list ul:last-child{width:200px}
.service-list li{display:flex;align-items:flex-start;gap:6px}
.tick{flex:none;display:inline-block;width:12px;height:12px;border:1px solid var(--tick);margin-top:4px;position:relative}
.tick::after{content:"";position:absolute;left:3px;top:0;width:4px;height:7px;border:solid var(--ink);border-width:0 2px 2px 0;transform:rotate(40deg)}
.general{position:absolute;left:532px;top:1060px;width:560px}
.general .section-title{font-size:40px;font-weight:400;padding-bottom:4px;border-bottom:2px solid var(--rule);display:inline-block;margin-bottom:10px}
.gallery{position:absolute;left:540px;top:1209px;width:550px;display:grid;grid-template-columns:repeat(3,1fr);grid-auto-rows:140px;gap:18px 16px}
.gallery div{background:linear-gradient(135deg,#6f6a64,#3e3c3a)}
.gallery div:nth-child(3){background:linear-gradient(135deg,#a4563f,#4a3a34)}
.gallery div:nth-child(5){background:linear-gradient(135deg,#c9cccd,#7a7e82)}
.left-col{position:absolute;left:40px;top:845px;width:450px;color:var(--ink)}
.left-block{margin-bottom:24px}
.left-title{font-family:"Roboto Condensed",sans-serif;font-weight:700;font-size:22px;line-height:1.05;text-transform:uppercase;display:flex;gap:8px;padding-bottom:4px;border-bottom:2px solid var(--rule);margin-bottom:8px}
.left-title svg{flex:none;margin-top:3px}
.lead{font-weight:700;font-size:15px;line-height:1.3;margin-left:28px;margin-bottom:4px}
.checks{list-style:none;font-family:"Roboto Condensed",sans-serif;font-size:14px;line-height:1.45;margin-left:28px;color:var(--ink)}
.checks li{display:flex;gap:5px;align-items:flex-start}
.checks.grid{display:grid;grid-template-columns:150px 150px}
.contact h3{font-family:"Roboto Condensed",sans-serif;font-weight:700;font-size:26px;padding-bottom:2px;border-bottom:2px solid var(--rule);display:inline-block;margin-bottom:10px}
.contact p{display:flex;align-items:center;gap:8px;font-size:15px;margin-bottom:8px}
.contact .phones{font-size:20px;gap:10px}
.icon{width:20px;height:20px;flex:none}
.footer{position:absolute;left:0;bottom:0;width:1120px;height:56px;background:var(--panel);display:flex;align-items:center;justify-content:center;color:#fff;font-size:28px}
.footer b{font-weight:700}
</style>
</head>
<body>
<main class="flyer">
  <div class="hero-photo" role="img" aria-label="Photograph of large rolled steel coils in a workshop"></div>
  <div class="brand-box"><span class="brand-mark"></span><span class="brand-name">Corbin Sheetmetal</span></div>

  <section class="about">
    <h2>A BIT ABOUT US</h2>
    <p>Fast, friendly, and fully functional, our professional Metal Fabrication Service is well renowned throughout South Australia. Our team is up for every job, managing projects with the skill and experience our clients have come to expect. We always stand behind our work, custom made with pride.<br>Established in 1991, we are suppliers to the plumbing and mining trades, shop-fitters and builders, and the general public. We provide general sheetmetal and light steel fabrication services (cutting, folding, mig/tig welding) working with stainless steel, copper, galvanised steel, aluminium and mild steel.</p>
    <p>As specialists in custom one-off and small-run manufacturing, take a look at some of our finished work and contact us with your enquiries.</p>
  </section>

  <div class="pride-band"><h1>Made with Pride</h1></div>

  <section class="services">
    <h2 class="section-title">SERVICES</h2>
    <p class="body-text">We can produce and supply a range of sheet metal components for all industries. We supply to the plumbing, mining trades, shop-fitters, builders, and the general public. We provide general sheetmetal and light steel fabrication services (cutting, folding, mig/tig welding) working with stainless steel, aluminium, copper, galvanised steel and mild steel.</p>
    <div class="service-list">
      <ul>
        <li><span class="tick"></span>Commercial kitchen canopies</li>
        <li><span class="tick"></span>Shelvng</li>
        <li><span class="tick"></span>Tanks</li>
        <li><span class="tick"></span>Silt traps</li>
        <li><span class="tick"></span>Brackets</li>
        <li><span class="tick"></span>Mild Steel / Frame Work</li>
      </ul>
      <ul>
        <li><span class="tick"></span>Bench tops</li>
        <li><span class="tick"></span>Safety trays</li>
        <li><span class="tick"></span>Tundishes</li>
        <li><span class="tick"></span>Hand rails</li>
        <li><span class="tick"></span>Most Stainless Steel components</li>
        <li><span class="tick"></span>Duct Work</li>
      </ul>
    </div>
  </section>

  <section class="general">
    <h2 class="section-title">General Fabrication</h2>
    <p class="body-text">Wether you're performing shop fabrication, repairing equipment on a farm or job site, or creating artwork in your garage, Corbin Sheetmetal has the knowhow, creativity and process knowledge to help you get your job done right.</p>
  </section>

  <div class="gallery">
    <div role="img" aria-label="Welder at work in high-visibility vest"></div>
    <div role="img" aria-label="Welded steel frame"></div>
    <div role="img" aria-label="Fabricated steel grill racks"></div>
    <div role="img" aria-label="Stainless steel cabinet frame"></div>
    <div role="img" aria-label="Stainless steel ducting"></div>
    <div role="img" aria-label="Sheetmetal enclosure in workshop"></div>
  </div>

  <section class="left-col">
    <div class="left-block">
      <h3 class="left-title"><svg width="16" height="16" viewBox="0 0 16 16"><path d="M2 3l10 5-10 5" fill="none" stroke="#1d1d21" stroke-width="2"/></svg><span>Facilities, materials and finishes<br>we have an exte</span></h3>
      <p class="lead">We have an extensive range of equipment and sheet metal machinery that includes:</p>
      <ul class="checks">
        <li><span class="tick"></span>Hydraulic Pressbrake and Guillotine</li>
        <li><span class="tick"></span>Pendrawn Copy Punch and notcher</li>
        <li><span class="tick"></span>Mechanical folders and plate roll</li>
        <li><span class="tick"></span>Extensive TIG and MIG welding equipment</li>
      </ul>
    </div>
    <div class="left-block">
      <h3 class="left-title"><svg width="16" height="16" viewBox="0 0 16 16"><path d="M2 3l10 5-10 5" fill="none" stroke="#1d1d21" stroke-width="2"/></svg><span>We fabricate a range of materials<br>including:</span></h3>
      <ul class="checks grid">
        <li><span class="tick"></span>Stainless Steel</li>
        <li><span class="tick"></span>Aluminium</li>
        <li><span class="tick"></span>Galvanised</li>
        <li><span class="tick"></span>Mild Steel</li>
        <li style="grid-column:2 / 3;margin-left:-40px"><span class="tick"></span>Brass</li>
      </ul>
    </div>
    <div class="left-block">
      <h3 class="left-title" style="text-transform:none"><svg width="16" height="16" viewBox="0 0 16 16"><path d="M2 3l10 5-10 5" fill="none" stroke="#1d1d21" stroke-width="2"/></svg><span>Finishes include:</span></h3>
      <ul class="checks grid">
        <li><span class="tick"></span>Polished</li>
        <li><span class="tick"></span>Painted</li>
        <li><span class="tick"></span>Powder-Coated</li>
        <li><span class="tick"></span>Mirrored</li>
        <li><span class="tick"></span>Textured</li>
      </ul>
    </div>
    <div class="contact">
      <h3>CONTACT US</h3>
      <p><svg class="icon" viewBox="0 0 20 20"><circle cx="10" cy="10" r="9.5" fill="#1d1d21"/><path d="M10 4a3.5 3.5 0 0 0-3.5 3.5C6.5 10 10 15 10 15s3.5-5 3.5-7.5A3.5 3.5 0 0 0 10 4z" fill="#fff"/><circle cx="10" cy="7.5" r="1.3" fill="#1d1d21"/></svg>17 Forge Street, Kilburn SA 5084, Australia</p>
      <p><svg class="icon" viewBox="0 0 20 20"><circle cx="10" cy="10" r="9.5" fill="#1d1d21"/><rect x="5" y="6.5" width="10" height="7" fill="#fff"/><path d="M5 6.5l5 4 5-4" fill="none" stroke="#1d1d21" stroke-width="1"/></svg>info@corbinsheetmetal.example</p>
      <p class="phones"><svg class="icon" viewBox="0 0 20 20"><circle cx="10" cy="10" r="9" fill="none" stroke="#1d1d21" stroke-width="1.5"/><path d="M7 5.5l2 2-1 1.2c.6 1.4 1.6 2.4 3 3l1.2-1 2 2-1.2 1.5c-3.5-.5-6.5-3.5-7-7z" fill="#1d1d21"/></svg>(08) 8100 4521&nbsp;&nbsp;&nbsp;<svg class="icon" viewBox="0 0 20 20"><circle cx="10" cy="10" r="9" fill="none" stroke="#1d1d21" stroke-width="1.5"/><path d="M7 5.5l2 2-1 1.2c.6 1.4 1.6 2.4 3 3l1.2-1 2 2-1.2 1.5c-3.5-.5-6.5-3.5-7-7z" fill="#1d1d21"/></svg>08 8100 4522</p>
    </div>
  </section>

  <footer class="footer"><span>www.<b>corbinsheetmetal</b>.example</span></footer>
</main>
</body>
</html>
```